Webdesign für Reisebüro
Zielgruppe
Reisebüro - wir haben uns vor 20 Jahren auf Reisen nach Asien spezialisiert aber inzwischen ist unsere Kernkompetenz das individuelle Arrangieren von Fernreisen in alle Welt. Jedoch decken wir auch das komplette touristische Portfolio ab was natürlich auch nicht zu kurz kommen darf. Unsere Zielgruppe liegt tatsächlich zwischen 20—70
Aufgabenstellung
Wir bezeichnen uns als das besondere Reisebüro weil wir als Menschen besonders sind. Wir lieben es zu begeistern und das gelingt uns so gut dass wir seit bestimmt 15 Jahren komplett ohne Werbung auskommen und nur von Mundpropaganda leben. Das Design soll genau dieses Besondere zum Ausdruck bringen. Soll keine „klassische“ Reisebüroseite sein auf der man selbst Reisen suchen Und buchen kann.
Natürlich wird es zb eine Seite „Über uns“ und Zielgebietsinfos und noch andere Seiten geben. Primär geht es jetzt mal um das Design an sich das unser Programmierer dann sicher umsetzen kann.
Das Büro ist bisschen im Factory Style eingerichtet und wird aktuell noch mehr diesem Style angepasst.
Der Name Wander Nest spiegelt den chilligen Lifestyle wieder den wir verkörpern.

```html
<!DOCTYPE html>
<html lang="de">
<head>
<meta charset="utf-8">
<title>Wander Nest – Webdesign</title>
<link href="https://fonts.googleapis.com/css2?family=Raleway:wght@300;400&family=Dancing+Script:wght@500;700&family=Oswald:wght@300&display=swap" rel="stylesheet">
<style>
  :root{
    --stage:#474d52;
    --slate:#474e53;
    --ink:#4a5055;
    --sand:#c2b0a6;
    --teal:#82a09f;
    --teal-dark:#6d8f8e;
    --paper:#efefed;
    --rust:#b9633f;
    --alert:#a3201c;
    --note:#e0141b;
    --white:#ffffff;
  }
  *{margin:0;padding:0;box-sizing:border-box}
  html,body{width:918px;height:1200px;overflow:hidden}
  body{background:var(--stage);position:relative;font-family:'Raleway',sans-serif;color:var(--ink)}

  .note{position:absolute;font-family:'Oswald',sans-serif;font-weight:300;color:var(--note);font-size:12px;line-height:17px;letter-spacing:-.2px}
  .note--carousel{left:41px;top:213px}
  .note--fly-in{left:33px;top:656px;width:80px}

  .page{position:absolute;left:153px;top:100px;width:611px;height:999px;background:var(--white);box-shadow:0 6px 18px rgba(0,0,0,.55);overflow:hidden}

  .hero{position:absolute;left:0;top:0;width:611px;height:426px}
  .hero__map{position:absolute;inset:0}
  .hero__title{position:absolute;left:0;top:0;width:611px;height:426px}
  .hero__rule{position:absolute;height:2px;background:var(--ink)}
  .hero__rule--top{left:349px;top:122px;width:154px}
  .hero__rule--bottom{left:290px;top:242px;width:154px}
  .hero__script{position:absolute;left:334px;top:121px;font-family:'Dancing Script',cursive;font-weight:700;font-size:40px;color:var(--ink);letter-spacing:-.5px}
  .hero__line{position:absolute;font-weight:400;font-size:23px;color:var(--ink);letter-spacing:.5px}
  .hero__line--one{left:331px;top:178px}
  .hero__line--two{left:342px;top:206px}

  .topbar{position:absolute;left:0;top:12px;width:611px;height:28px;background:rgba(255,255,255,.85)}
  .brand{position:absolute;left:20px;top:3px;width:54px;height:54px;border-radius:50%;background:var(--white);border:1.5px solid var(--ink);display:flex;align-items:center;justify-content:center;text-align:center;font-size:9px;line-height:10px;font-weight:400;color:var(--ink)}
  .nav{position:absolute;left:144px;top:20px;display:flex;gap:12px;font-size:7.8px;font-weight:400;color:var(--ink)}
  .social{position:absolute;left:458px;top:19px;display:flex;gap:5.5px}
  .social span{width:14px;height:14px;background:#b3aaa4;display:block}
  .social svg{display:block}

  .section-head{position:absolute;left:0;width:611px;display:flex;align-items:center;justify-content:center;font-weight:400;letter-spacing:1px}
  .section-head--trips{top:426px;height:77px;background:var(--sand);color:var(--ink);font-size:36px}
  .section-head--about{top:637px;height:76px;background:var(--teal);color:var(--white);font-size:36px}

  .trips{position:absolute;left:0;top:503px;width:611px;height:134px;background:var(--slate)}
  .trip{position:absolute;top:0;width:139px;height:134px}
  .trip__photo{position:absolute;left:0;top:0;width:139px;height:92px}
  .trip__label{position:absolute;left:0;top:92px;width:97px;height:42px;display:flex;align-items:center;justify-content:center;color:var(--white);font-size:11.5px;letter-spacing:.3px}
  .trip__label--left{justify-content:flex-start}
  .trip__go{position:absolute;left:97px;top:92px;width:42px;height:42px;background:var(--sand)}
  .trip__badge{position:absolute;right:0;top:9px;width:42px;height:13px;background:var(--alert);color:var(--white);font-size:10px;line-height:13px;padding-left:1px}

  .about{position:absolute;left:0;top:713px;width:611px;height:174px;background:var(--paper)}
  .about__kicker{position:absolute;left:55px;top:26px;font-family:'Dancing Script',cursive;font-weight:500;font-size:15px;color:var(--teal-dark)}
  .about__text{position:absolute;font-size:8px;line-height:10.6px;font-weight:300;color:var(--ink)}
  .about__text--left{left:57px;top:66px}
  .about__text--right{left:384px;top:26px}
  .about__photo{position:absolute;left:249px;top:16px;width:105px;height:139px}

  .claim{position:absolute;left:0;top:887px;width:611px;height:75px;background:var(--teal);display:flex;align-items:center;justify-content:center;color:#f2f5f5;font-weight:300;font-size:17px}

  .footer{position:absolute;left:0;top:962px;width:611px;height:37px;background:var(--rust);color:#f3ded3;font-size:6px;font-weight:300}
  .footer__hours-extra{position:absolute;left:345px;top:7px}
  .footer__line{position:absolute;left:37px;top:19px;white-space:pre}
</style>
</head>
<body>
  <p class="note note--carousel">Hier Carousel --&gt;</p>
  <p class="note note--fly-in">Hier einfliegend von links ------&gt;</p>

  <main class="page">
    <section class="hero">
      <svg class="hero__map" width="611" height="426" role="img" aria-label="Weltkarte aus freigelegten Ziegelsteinen auf weiß verputzter Wand">
        <defs>
          <linearGradient id="wall" x1="0" y1="0" x2="1" y2="1">
            <stop offset="0" stop-color="#d9d6d4"/>
            <stop offset=".35" stop-color="#cf9a83"/>
            <stop offset=".55" stop-color="#d8c2b8"/>
            <stop offset=".8" stop-color="#cf9378"/>
            <stop offset="1" stop-color="#dedad8"/>
          </linearGradient>
        </defs>
        <rect width="611" height="426" fill="url(#wall)"/>
        <polygon points="390,0 590,0 270,426 80,426" fill="#ffffff" opacity=".35"/>
      </svg>
      <div class="hero__title">
        <div class="hero__rule hero__rule--top"></div>
        <div class="hero__script">Traumziele</div>
        <div class="hero__line hero__line--one">weltweit</div>
        <div class="hero__line hero__line--two">entdecken</div>
        <div class="hero__rule hero__rule--bottom"></div>
      </div>
    </section>

    <header class="topbar">
      <nav class="nav">
        <span>Reisen</span><span>Über uns</span><span>Kontakt</span><span>Impressum</span><span>Datenschutz</span>
      </nav>
      <div class="social">
        <span></span><span></span><span></span><span></span>
        <span><svg width="14" height="14" viewBox="0 0 14 14"><path d="M4.3 3.2l1.3-.3.8 2-1 .7c.5 1.1 1.3 1.9 2.4 2.4l.7-1 2 .8-.3 1.3c-3.3.2-6.1-2.6-5.9-5.9z" fill="#fff"/></svg></span>
      </div>
    </header>
    <div class="brand">Wander<br>Nest</div>

    <h2 class="section-head section-head--trips">REISEN</h2>

    <section class="trips">
      <article class="trip" style="left:16px">
        <div class="trip__photo" role="img" aria-label="Longtailboot vor grüner Insel in Thailand" style="background:linear-gradient(180deg,#8fb4d6 0%,#4d7a4a 45%,#4e9bb4 70%,#c8472c 100%)"></div>
        <div class="trip__label trip__label--left">THAILAND</div>
        <svg class="trip__go" width="42" height="42"><polygon points="10,13 33,21 10,29 16,21" fill="#fff"/></svg>
      </article>
      <article class="trip" style="left:160px">
        <div class="trip__photo" role="img" aria-label="Brooklyn Bridge und Skyline am Wasser" style="background:linear-gradient(180deg,#8ea6bf 0%,#b8c3c9 45%,#8a7a62 65%,#4f6277 100%)"></div>
        <div class="trip__label">USA</div>
        <svg class="trip__go" width="42" height="42"><polygon points="10,13 33,21 10,29 16,21" fill="#fff"/></svg>
      </article>
      <article class="trip" style="left:303px">
        <div class="trip__photo" role="img" aria-label="Kanadische Berglandschaft mit Wald und Wiese" style="background:linear-gradient(180deg,#c9d2da 0%,#7c8a7e 35%,#3f5b39 60%,#8ba640 100%)"></div>
        <div class="trip__badge">NEU</div>
        <div class="trip__label">KANADA</div>
        <svg class="trip__go" width="42" height="42"><polygon points="10,13 33,21 10,29 16,21" fill="#fff"/></svg>
      </article>
      <article class="trip" style="left:447px">
        <div class="trip__photo" role="img" aria-label="Violette Seerose im dunklen Teich" style="background:radial-gradient(circle at 50% 40%,#8a5fc0 0%,#3c4a2c 30%,#1f2a22 100%)"></div>
        <div class="trip__label">SRI LANKA</div>
        <svg class="trip__go" width="42" height="42"><polygon points="10,13 33,21 10,29 16,21" fill="#fff"/></svg>
      </article>
    </section>

    <h2 class="section-head section-head--about">ÜBER UNS</h2>

    <section class="about">
      <h3 class="about__kicker">Wer wir sind</h3>
      <p class="about__text about__text--left">Das Wander Nest in Augsburg ist<br>ein inhabergeführtes Reisebüro<br>im Herzen von Augsburg.<br>Bei uns werden Sie individuell<br>und sehr ausführlich beraten,<br>damit Ihre Reiseplanungen<br>garantiert zum Erfolg werden.</p>
      <div class="about__photo" role="img" aria-label="Theke des Reisebüros im Factory Style mit Pflanzen und Hängelampe" style="background:linear-gradient(180deg,#c9cbc4 0%,#8a8672 40%,#b2936e 70%,#8c4c36 100%)"></div>
      <p class="about__text about__text--right">Wir freuen uns wenn Sie das<br>Wander Nest besuchen.<br>Unsere Spezialgebiet sind Reisen<br>in all asiatischen Länder wie<br>Thailand, Vietnam, China und Indien,<br>aber wir sind auf der ganzen Welt<br>zu Hause.<br>Egal ob eine Städtereise in Europa,<br>&nbsp;ein Trip in die USA oder Kanada, oder<br>der Event zum nächsten Heimspiel<br>Ihres Lieblingsvereins.</p>
    </section>

    <p class="claim">Wir machen Ihre Reise zu einem unvergesslichen Erlebnis.</p>

    <footer class="footer">
      <span class="footer__hours-extra">Mi -Vormittag :&nbsp;&nbsp;geschlossen</span>
      <span class="footer__line">2019 - Wander Nest  Lindenweg 4, 86150 Augsburg - Tel. 0821-4400120     -     ÖFFNUNGSZEITEN :  Mo-Fr.   10 - 13 h /14 - 18 h   Sa.  10 - 13 h        info@wander-nest.de</span>
    </footer>
  </main>
</body>
</html>
```